Global Beard Oil Review Business needs a refresh

topwhiskerbalm.net is a global business who's mission is to curate all available beard oils from around the world, review and grade them and present this curated collection to the user of the website.

The scope of this job includes the web site design and the design of a suitable logo to be used in the site header.

The existing site can be seen on http://topwhiskerbalm.net, however this is a mock-up only the style and logo should NOT be used. This is to give you an idea of the concept of the site only.

This job is for PSD design only.

See attached design brief for detailed design requirements.
Updates

Target Market(s)

Men's grooming / retail

Industry/Entity Type

Retail

Number of Pages Required

2 page

Font styles to use
Sans Serif

Requirements
Must have
• 1) Comparison Table
• 2) Side Bar
• 3) Header area
• 4) Photo of Lomax Penhallow (attached - can be circular or "cut-out")
• 5) Cool beard-oriented custom design background (e.g., stylistic black/brown on brown/orange beard background. I envision this beard background "drawing" rather than photo based)
• (see attached design requirements for details)
Nice to have
• Signature style writing at top with name "Lomax Penhallow"
Should not have
• Do NOT use the look & feel or logo from the existing site.

```html
<!DOCTYPE html>
<html lang="en">
<head>
<meta charset="utf-8">
<title>Top Whisker Balm – Global Beard Oil Review</title>
<link href="https://fonts.googleapis.com/css2?family=Oswald:wght@400;500&family=Roboto:wght@400;500&family=Dancing+Script:wght@500&display=swap" rel="stylesheet">
<style>
:root{
  --orange:#e8870a;
  --orange-light:#f5a227;
  --green:#0d5a35;
  --text:#333333;
  --muted:#555555;
  --head-dark:#4a4a4a;
  --row-a:#f5f5f5;
  --row-b:#ececec;
  --footer:#5d5d5d;
  --footer-bottom:#141414;
  --white:#ffffff;
}
*{box-sizing:border-box;margin:0;padding:0}
html,body{width:1200px;height:2510px;overflow:hidden}
body{position:relative;background:var(--white);font-family:'Roboto',Arial,sans-serif;color:var(--text)}
ul{list-style:none}

/* header */
.site-header{position:absolute;left:0;top:0;width:1200px;height:104px;background:var(--white)}
.logo{position:absolute;left:79px;top:38px;font-family:'Oswald',Arial,sans-serif;font-weight:500;font-size:30px;line-height:40px;color:var(--green);letter-spacing:.5px}
.main-nav{position:absolute;top:46px;left:547px;display:flex;gap:32px;font-size:13px;color:var(--muted);text-transform:uppercase;letter-spacing:.3px}
.btn-login{position:absolute;left:1051px;top:38px;width:74px;height:32px;background:linear-gradient(#f39a1e,var(--orange));color:var(--white);font-size:13px;font-weight:500;text-align:center;line-height:32px;border-radius:2px}

/* hero */
.hero{position:absolute;left:0;top:104px;width:1200px;height:498px;overflow:hidden}
.hero-photo{position:absolute;inset:0;background:linear-gradient(90deg,#d8d7d3 0%,#cfceca 45%,#8d8f96 68%,#4d5462 82%,#c9c8c4 100%)}
.hero-title{position:absolute;left:87px;top:206px;font-family:'Oswald',Arial,sans-serif;font-weight:500;font-size:48px;line-height:58px;color:#2a2a2a}
.hero-signature{position:absolute;left:87px;top:268px;font-family:'Dancing Script',cursive;font-size:38px;color:var(--green)}

/* comparison table */
.review-table{position:absolute;left:75px;top:653px;width:802px;border-collapse:collapse;table-layout:fixed;font-size:11px;color:var(--text)}
.review-table .group-row th{height:42px;background:var(--orange);color:var(--white);font-weight:400;font-size:13px;letter-spacing:.5px;border-right:1px solid #f6c27d}
.review-table .group-row th:last-child{border-right:0}
.review-table .col-row th{height:53px;background:linear-gradient(#5a5a5a,#3f3f3f);color:#eeeeee;font-weight:400;font-size:12px;line-height:14px}
.review-table td{height:73px;text-align:center;vertical-align:middle;border-top:1px solid #ffffff}
.review-table tbody tr:nth-child(odd) td{background:var(--row-a)}
.review-table tbody tr:nth-child(even) td{background:var(--row-b)}
.review-table .supplier{line-height:13px}
.bottle{display:inline-block;width:16px;height:36px;border-radius:4px 4px 3px 3px;background:linear-gradient(#7a4a2a 0 22%,#c98a55 22% 100%)}
.btn-buy{display:inline-block;width:70px;height:24px;line-height:24px;border-radius:3px;background:linear-gradient(var(--orange-light),var(--orange));color:var(--white);font-size:9px;font-weight:500;border:1px solid #d67a05}
.table-frame{position:absolute;left:75px;top:653px;width:802px;height:1558px;border:1px solid #d8d8d8;pointer-events:none}

/* sidebar */
.sidebar{position:absolute;left:884px;top:650px;width:248px;height:731px;background:var(--white);box-shadow:0 0 4px rgba(0,0,0,.2)}
.sidebar-title{height:45px;background:var(--green);color:var(--white);font-size:14px;line-height:45px;padding-left:17px;letter-spacing:.3px}
.blog-item{margin:0 12px 0 14px;padding:12px 0 10px;border-bottom:1px solid #dddddd;height:131px}
.blog-item h3{font-weight:400;font-size:13.5px;color:#222;line-height:18px}
.blog-date{font-size:10px;color:var(--orange);margin-top:6px}
.blog-item p{font-size:9.5px;line-height:15px;color:var(--muted);margin-top:6px;text-align:justify}
.read-more{font-size:9.5px;color:var(--orange);margin-top:5px;display:block}
.view-more{display:block;text-align:center;font-size:10px;color:var(--orange);margin-top:10px}

/* footer */
.site-footer{position:absolute;left:0;top:2248px;width:1200px;height:204px;background:var(--footer);color:#e6e6e6}
.footer-col{position:absolute;top:40px}
.footer-col h4{font-weight:400;font-size:15px;color:var(--white);letter-spacing:.3px;margin-bottom:14px}
.footer-col p,.footer-col li{font-size:11px;line-height:21px}
.footer-col li::before{content:"▸";font-size:8px;margin-right:6px;color:#dddddd}
.newsletter p{line-height:14px;width:200px}
.email-input{margin-top:6px;width:184px;height:26px;background:var(--white);color:#888;font-size:10px;line-height:26px;padding-left:8px}
.btn-subscribe{margin-top:10px;width:84px;height:24px;background:linear-gradient(var(--orange-light),var(--orange));color:var(--white);font-size:10px;line-height:24px;text-align:center;border-radius:2px}
.contact p{line-height:21px}
.social li::before{content:none}
.social li{display:flex;align-items:center;height:36px;gap:12px}
.social-circle{width:30px;height:30px;border:1px solid #cfcfcf;border-radius:50%}
.footer-bottom{position:absolute;left:0;top:2452px;width:1200px;height:58px;background:var(--footer-bottom);color:#dddddd;font-size:10px;text-align:center;line-height:58px}
</style>
</head>
<body>

<header class="site-header">
  <div class="logo">TOP WHISKER BALM</div>
  <ul class="main-nav">
    <li>Home</li><li>Our Charter</li><li>Beard Oil Review Methodology</li><li>Blog</li>
  </ul>
  <div class="btn-login">LOGIN</div>
</header>

<section class="hero">
  <div class="hero-photo" role="img" aria-label="Photo of a bearded man in a checked shirt against a white brick wall"></div>
  <h1 class="hero-title">GLOBAL BEARD OIL REVIEW</h1>
  <div class="hero-signature">With Lomax Penhallow</div>
</section>

<table class="review-table">
  <colgroup>
    <col style="width:80px"><col style="width:88px"><col style="width:66px"><col style="width:88px"><col style="width:80px"><col style="width:64px">
    <col style="width:66px"><col style="width:64px"><col style="width:60px"><col style="width:61px"><col style="width:85px">
  </colgroup>
  <thead>
    <tr class="group-row"><th colspan="6">INFORMATION</th><th colspan="4">REVIEW</th><th>LINK</th></tr>
    <tr class="col-row"><th>Supplier</th><th>Name</th><th>Photo</th><th>Origin</th><th>Base Oil</th><th>Scent</th><th>Aroma</th><th>Therapeutic Affect</th><th>Value</th><th>Overall</th><th>Link</th></tr>
  </thead>
  <tbody>
    <tr><td class="supplier">Bristle<br>Baron</td><td>Timberline</td><td><span class="bottle" role="img" aria-label="Beard oil bottle"></span></td><td>USA</td><td>Neque porro</td><td>quisquam est</td><td>7</td><td>5</td><td>3</td><td>6</td><td><span class="btn-buy">BUY NOW</span></td></tr>
    <tr><td class="supplier">Bristle<br>Baron</td><td>Timberline</td><td><span class="bottle" role="img" aria-label="Beard oil bottle"></span></td><td>USA</td><td>Neque porro</td><td>quisquam est</td><td>7</td><td>5</td><td>3</td><td>6</td><td><span class="btn-buy">BUY NOW</span></td></tr>
    <tr><td class="supplier">Bristle<br>Baron</td><td>Timberline</td><td><span class="bottle" role="img" aria-label="Beard oil bottle"></span></td><td>USA</td><td>Neque porro</td><td>quisquam est</td><td>7</td><td>5</td><td>3</td><td>6</td><td><span class="btn-buy">BUY NOW</span></td></tr>
    <tr><td class="supplier">Bristle<br>Baron</td><td>Timberline</td><td><span class="bottle" role="img" aria-label="Beard oil bottle"></span></td><td>USA</td><td>Neque porro</td><td>quisquam est</td><td>7</td><td>5</td><td>3</td><td>6</td><td><span class="btn-buy">BUY NOW</span></td></tr>
    <tr><td class="supplier">Bristle<br>Baron</td><td>Timberline</td><td><span class="bottle" role="img" aria-label="Beard oil bottle"></span></td><td>USA</td><td>Neque porro</td><td>quisquam est</td><td>7</td><td>5</td><td>3</td><td>6</td><td><span class="btn-buy">BUY NOW</span></td></tr>
    <tr><td class="supplier">Bristle<br>Baron</td><td>Timberline</td><td><span class="bottle" role="img" aria-label="Beard oil bottle"></span></td><td>USA</td><td>Neque porro</td><td>quisquam est</td><td>7</td><td>5</td><td>3</td><td>6</td><td><span class="btn-buy">BUY NOW</span></td></tr>
    <tr><td class="supplier">Bristle<br>Baron</td><td>Timberline</td><td><span class="bottle" role="img" aria-label="Beard oil bottle"></span></td><td>USA</td><td>Neque porro</td><td>quisquam est</td><td>7</td><td>5</td><td>3</td><td>6</td><td><span class="btn-buy">BUY NOW</span></td></tr>
    <tr><td class="supplier">Bristle<br>Baron</td><td>Timberline</td><td><span class="bottle" role="img" aria-label="Beard oil bottle"></span></td><td>USA</td><td>Neque porro</td><td>quisquam est</td><td>7</td><td>5</td><td>3</td><td>6</td><td><span class="btn-buy">BUY NOW</span></td></tr>
    <tr><td class="supplier">Bristle<br>Baron</td><td>Timberline</td><td><span class="bottle" role="img" aria-label="Beard oil bottle"></span></td><td>USA</td><td>Neque porro</td><td>quisquam est</td><td>7</td><td>5</td><td>3</td><td>6</td><td><span class="btn-buy">BUY NOW</span></td></tr>
    <tr><td class="supplier">Bristle<br>Baron</td><td>Timberline</td><td><span class="bottle" role="img" aria-label="Beard oil bottle"></span></td><td>USA</td><td>Neque porro</td><td>quisquam est</td><td>7</td><td>5</td><td>3</td><td>6</td><td><span class="btn-buy">BUY NOW</span></td></tr>
    <tr><td class="supplier">Bristle<br>Baron</td><td>Timberline</td><td><span class="bottle" role="img" aria-label="Beard oil bottle"></span></td><td>USA</td><td>Neque porro</td><td>quisquam est</td><td>7</td><td>5</td><td>3</td><td>6</td><td><span class="btn-buy">BUY NOW</span></td></tr>
    <tr><td class="supplier">Bristle<br>Baron</td><td>Timberline</td><td><span class="bottle" role="img" aria-label="Beard oil bottle"></span></td><td>USA</td><td>Neque porro</td><td>quisquam est</td><td>7</td><td>5</td><td>3</td><td>6</td><td><span class="btn-buy">BUY NOW</span></td></tr>
    <tr><td class="supplier">Bristle<br>Baron</td><td>Timberline</td><td><span class="bottle" role="img" aria-label="Beard oil bottle"></span></td><td>USA</td><td>Neque porro</td><td>quisquam est</td><td>7</td><td>5</td><td>3</td><td>6</td><td><span class="btn-buy">BUY NOW</span></td></tr>
    <tr><td class="supplier">Bristle<br>Baron</td><td>Timberline</td><td><span class="bottle" role="img" aria-label="Beard oil bottle"></span></td><td>USA</td><td>Neque porro</td><td>quisquam est</td><td>7</td><td>5</td><td>3</td><td>6</td><td><span class="btn-buy">BUY NOW</span></td></tr>
    <tr><td class="supplier">Bristle<br>Baron</td><td>Timberline</td><td><span class="bottle" role="img" aria-label="Beard oil bottle"></span></td><td>USA</td><td>Neque porro</td><td>quisquam est</td><td>7</td><td>5</td><td>3</td><td>6</td><td><span class="btn-buy">BUY NOW</span></td></tr>
    <tr><td class="supplier">Bristle<br>Baron</td><td>Timberline</td><td><span class="bottle" role="img" aria-label="Beard oil bottle"></span></td><td>USA</td><td>Neque porro</td><td>quisquam est</td><td>7</td><td>5</td><td>3</td><td>6</td><td><span class="btn-buy">BUY NOW</span></td></tr>
    <tr><td class="supplier">Bristle<br>Baron</td><td>Timberline</td><td><span class="bottle" role="img" aria-label="Beard oil bottle"></span></td><td>USA</td><td>Neque porro</td><td>quisquam est</td><td>7</td><td>5</td><td>3</td><td>6</td><td><span class="btn-buy">BUY NOW</span></td></tr>
    <tr><td class="supplier">Bristle<br>Baron</td><td>Timberline</td><td><span class="bottle" role="img" aria-label="Beard oil bottle"></span></td><td>USA</td><td>Neque porro</td><td>quisquam est</td><td>7</td><td>5</td><td>3</td><td>6</td><td><span class="btn-buy">BUY NOW</span></td></tr>
    <tr><td class="supplier">Bristle<br>Baron</td><td>Timberline</td><td><span class="bottle" role="img" aria-label="Beard oil bottle"></span></td><td>USA</td><td>Neque porro</td><td>quisquam est</td><td>7</td><td>5</td><td>3</td><td>6</td><td><span class="btn-buy">BUY NOW</span></td></tr>
    <tr><td class="supplier">Bristle<br>Baron</td><td>Timberline</td><td><span class="bottle" role="img" aria-label="Beard oil bottle"></span></td><td>USA</td><td>Neque porro</td><td>quisquam est</td><td>7</td><td>5</td><td>3</td><td>6</td><td><span class="btn-buy">BUY NOW</span></td></tr>
  </tbody>
</table>
<div class="table-frame"></div>

<aside class="sidebar">
  <div class="sidebar-title">LATEST BLOG</div>
  <article class="blog-item"><h3>Neque porro quisquam est qui dolorem</h3><div class="blog-date">12 sep 2016</div><p>Lorem Ipsum has been the industry's standard dummy text ever since the 1500s, when an unknown printer took a galley</p><span class="read-more">Read More »</span></article>
  <article class="blog-item"><h3>Neque porro quisquam est qui dolorem</h3><div class="blog-date">12 sep 2016</div><p>Lorem Ipsum has been the industry's standard dummy text ever since the 1500s, when an unknown printer took a galley</p><span class="read-more">Read More »</span></article>
  <article class="blog-item"><h3>Neque porro quisquam est qui dolorem</h3><div class="blog-date">12 sep 2016</div><p>Lorem Ipsum has been the industry's standard dummy text ever since the 1500s, when an unknown printer took a galley</p><span class="read-more">Read More »</span></article>
  <article class="blog-item"><h3>Neque porro quisquam est qui dolorem</h3><div class="blog-date">12 sep 2016</div><p>Lorem Ipsum has been the industry's standard dummy text ever since the 1500s, when an unknown printer took a galley</p><span class="read-more">Read More »</span></article>
  <article class="blog-item"><h3>Neque porro quisquam est qui dolorem</h3><div class="blog-date">12 sep 2016</div><p>Lorem Ipsum has been the industry's standard dummy text ever since the 1500s, when an unknown printer took a galley</p><span class="read-more">Read More »</span></article>
  <span class="view-more">View more »</span>
</aside>

<footer class="site-footer">
  <div class="footer-col newsletter" style="left:77px">
    <h4>NEWSLETTERS SIGN UP</h4>
    <p>Sign up for our daily email by entering your information below</p>
    <div class="email-input">Email address</div>
    <div class="btn-subscribe">SUBSCRIBE</div>
  </div>
  <div class="footer-col" style="left:375px">
    <h4>LINKS</h4>
    <ul><li>Blog</li><li>Contact</li><li>Affiliate</li><li>General FAQs</li><li>Shortcodes</li></ul>
  </div>
  <div class="footer-col" style="left:554px">
    <h4>QUICK LINKS</h4>
    <ul><li>Home</li><li>Our Charter</li><li>Beard Oil Review Methodology</li><li>Blog</li></ul>
  </div>
  <div class="footer-col contact" style="left:775px">
    <h4>GET IN TOUCH</h4>
    <p>Address : 1420 Harbor Lane,<br>Millbrook, NJ</p>
    <p style="margin-top:6px">Phone : 201 555 0148</p>
    <p style="margin-top:6px">Email : info@samplemail.com</p>
  </div>
  <div class="footer-col" style="left:1024px">
    <h4>FOLLOW US ON</h4>
    <ul class="social">
      <li><span class="social-circle"></span>Friendbook</li>
      <li><span class="social-circle"></span>Chirper</li>
      <li><span class="social-circle"></span>Snapgram</li>
    </ul>
  </div>
</footer>
<div class="footer-bottom">Copyright © 2016. All Rights Reserved</div>

</body>
</html>
```